Business Landing Page for SEO Company

Need the landing page of the website designed - I will provide the copy, will need to include details of my company and the services offered, about us, testimonials, faq, etc., and all these elements will need to be arranged graphically on the page.

I want something similar to this: https://plorvantix.com/

Not in terms of color or theme or anything, but we offer a similar service and want to display similar information.

Th services we provide are:

Premium Links
Monthly Links Subscription
Link Insertions

Need to advertise them on the front page. Additionally need a place for testimonials, company details, etc.,

We already have logo for the website. Please use the attached file to insert the logo within the overal design.
Updates

Target Market(s)

SEO marketers and agencies

Number of Pages Required

1 page

```html
<!DOCTYPE html>
<html lang="en">
<head>
<meta charset="utf-8">
<title>Linkvora – SEO Link Building</title>
<link rel="stylesheet" href="https://fonts.googleapis.com/css2?family=Josefin+Sans:wght@400;600;700&family=Roboto:wght@400;500;700&display=swap">
<style>
:root{
  --orange:#ff6509;
  --blue:#2f78d6;
  --ink:#2b2b2b;
  --pale:#e6eefa;
  --footer:#121212;
  --white:#fff;
}
*{box-sizing:border-box;margin:0;padding:0}
html,body{width:1200px;height:4245px;overflow:hidden}
body{position:relative;font-family:"Josefin Sans",sans-serif;color:var(--ink);background:var(--white)}
.abs{position:absolute}
a{color:inherit;text-decoration:none}
.btn{display:inline-block;background:var(--orange);color:#fff;border-radius:30px;font-weight:600;text-transform:uppercase}
.btn-outline{display:inline-block;border:2px solid var(--orange);color:var(--orange);border-radius:30px;font-weight:600}
.heading{font-family:"Roboto",sans-serif;font-weight:500;color:var(--blue);text-transform:uppercase;letter-spacing:.5px}

/* header */
.site-header{left:0;top:0;width:1200px;height:102px;background:#fff}
.brand{font-family:"Josefin Sans",sans-serif;font-weight:600;color:var(--blue);white-space:nowrap}
.site-header .brand{left:78px;top:30px;font-size:40px;line-height:44px}
.nav{left:308px;top:43px;display:flex;gap:38px;font-size:15px;color:#333;white-space:nowrap}
.call{left:906px;top:25px;display:flex;align-items:center;gap:14px}
.call-icon{width:50px;height:50px;border-radius:50%;background:var(--orange);display:flex;align-items:center;justify-content:center}
.call small{display:block;color:var(--orange);font-size:12px}
.call strong{display:block;color:var(--blue);font-size:21px;font-weight:400;white-space:nowrap}

/* hero */
.hero{left:0;top:102px;width:1200px;height:689px;background:linear-gradient(90deg,#0f1a26 0%,#1a2b3c 55%,#2d4256 100%);overflow:hidden}
.hero-photo{position:absolute;right:0;top:0;width:520px;height:689px;background:radial-gradient(circle at 55% 40%,#4f7ea0 0%,#2a4156 40%,transparent 75%)}
.hero h1{position:absolute;left:108px;top:162px;font-size:52px;font-weight:600;color:#fff}
.hero p{position:absolute;left:108px;top:255px;width:580px;font-size:17px;line-height:30px;color:#fff}
.hero .btn{position:absolute;left:108px;top:340px;padding:16px 30px 13px;font-size:16px}
.hero svg{position:absolute;left:0;top:0}
.slider-dots{position:absolute;display:flex;gap:5px}
.slider-dots i{width:10px;height:10px;border-radius:50%;background:#fff}

/* about */
.about-photo{left:112px;top:887px;width:415px;height:445px}
.about-photo .frame{position:absolute;left:0;top:0;width:410px;height:440px;border-left:8px solid var(--orange);border-top:8px solid var(--orange)}
.about-photo .img{position:absolute;left:8px;top:8px;width:407px;height:437px;background:linear-gradient(160deg,#8e9ba6,#c9cfd4 45%,#5e6b76)}
.about-text{left:598px;top:908px;width:490px}
.about-text h2{font-size:34px}
.rule{width:100px;height:3px;background:var(--orange);margin:16px 0 26px}
.about-text p{font-size:15.5px;line-height:30px;color:#333}
.about-text .btn{margin-top:18px;padding:15px 31px 12px;font-size:16px}

/* services */
.services{left:0;top:1417px;width:1200px;height:706px;background:var(--pale)}
.services .title{position:absolute;left:112px;top:112px;font-size:34px;line-height:40px}
.vbar{position:absolute;width:3px;background:var(--orange)}
.services .intro{position:absolute;left:420px;top:102px;width:650px;font-size:16px;line-height:30px;color:#333}
.card{position:absolute;top:248px;width:308px;height:362px;background:#fff;box-shadow:0 0 6px rgba(0,0,0,.15);text-align:center;padding-top:30px}
.card h3{font-family:"Roboto",sans-serif;color:var(--blue);font-size:16px;font-weight:700;margin-top:14px;letter-spacing:.3px}
.card p{font-size:14px;line-height:30px;color:#444;padding:8px 26px 0}
.card .btn-outline{margin-top:14px;padding:14px 46px 11px;font-size:15px}

/* partners */
.partners{left:0;top:2123px;width:1200px;height:194px;background:var(--blue)}
.partner{position:absolute;top:64px;width:135px;height:66px;background:#fff;display:flex;align-items:center;justify-content:center}
.partner span{width:56px;height:30px;border-radius:4px;background:#cfd6df}

/* testimonials */
.testimonials .intro{left:130px;top:2412px;width:640px;font-size:16px;line-height:30px;text-align:right;color:#333}
.testimonials .title{left:830px;top:2420px;width:258px;font-size:34px;line-height:40px;text-align:right}
.quote{position:absolute;top:2546px;width:474px;height:321px;background:#fff;box-shadow:0 0 6px rgba(0,0,0,.18);padding:30px 24px}
.quote .mark{font-family:Georgia,serif;color:var(--orange);font-size:34px;font-style:italic;line-height:20px;height:22px}
.quote p{font-style:italic;font-size:16px;line-height:30px;color:#333}
.quote .who{margin-top:18px;color:var(--orange);font-size:19px}

/* blogs */
.blogs{left:0;top:3016px;width:1200px;height:877px;background:var(--pale)}
.blogs .title{position:absolute;left:0;top:90px;width:1200px;text-align:center;font-size:34px}
.blogs .rule{position:absolute;left:550px;top:136px;margin:0}
.blogs .intro{position:absolute;left:200px;top:150px;width:800px;text-align:center;font-size:16px;line-height:30px;color:#333}
.feature-img{position:absolute;left:112px;top:234px;width:478px;height:310px;background:linear-gradient(135deg,#d9dde2,#9aa5b0 50%,#5e6a74)}
.date{position:absolute;left:120px;top:242px;width:74px;height:74px;border-radius:50%;background:var(--orange);color:#fff;text-align:center;font-size:14px;line-height:17px;padding-top:10px}
.date small{display:block;font-size:10px}
.feature h3{position:absolute;left:119px;top:566px;width:470px;font-family:"Roboto",sans-serif;font-weight:400;font-size:26px;line-height:30px;color:#222}
.feature p{position:absolute;left:119px;top:634px;width:470px;font-size:14px;line-height:30px;color:#333}
.feature .btn{position:absolute;left:119px;top:730px;padding:12px 16px 9px;font-size:16px;text-transform:none;font-weight:400}
.post{position:absolute;left:601px;width:500px;height:172px}
.post .thumb{position:absolute;left:0;top:0;width:182px;height:170px;background:linear-gradient(160deg,#c4ccd4,#6f7b86)}
.post h4{position:absolute;left:198px;top:38px;font-size:16px;font-weight:700;color:#222}
.post p{position:absolute;left:198px;top:60px;width:300px;font-size:14px;line-height:30px;color:#444}

/* footer */
.site-footer{left:0;top:3893px;width:1200px;height:352px;background:var(--footer);color:#fff}
.site-footer .brand{position:absolute;left:112px;top:66px;font-size:44px;line-height:48px}
.socials{position:absolute;left:114px;top:170px;display:flex;gap:24px}
.socials span{width:32px;height:32px;border-radius:50%;background:#fff}
.fcol{position:absolute;top:64px;font-size:16px;line-height:30px}
.fcol h5{font-size:17px;font-weight:700;letter-spacing:1px;margin-bottom:6px}
.fcol li{list-style:none}
.fcol li::before{content:"» ";}
.contact li::before{content:none}
.contact li{display:flex;gap:12px;margin-bottom:8px;align-items:flex-start}
.contact svg{margin-top:5px;flex:none}
.site-footer hr{position:absolute;left:74px;top:265px;width:1050px;border:0;border-top:1px solid #555}
.copy{position:absolute;left:0;top:287px;width:1200px;text-align:center;font-size:16px}
</style>
</head>
<body>

<header class="site-header abs">
  <div class="brand abs">Linkvora</div>
  <nav class="nav abs">
    <a href="#">Home</a><a href="#">About Us</a><a href="#">Services</a><a href="#">Testimonials</a><a href="#">FAQ</a><a href="#">Contact Us</a>
  </nav>
  <div class="call abs">
    <div class="call-icon"><svg width="20" height="20" viewBox="0 0 24 24"><path fill="#fff" d="M6.6 10.8a15.1 15.1 0 0 0 6.6 6.6l2.2-2.2a1 1 0 0 1 1-.25 11.4 11.4 0 0 0 3.6.57 1 1 0 0 1 1 1V20a1 1 0 0 1-1 1A17 17 0 0 1 3 4a1 1 0 0 1 1-1h3.5a1 1 0 0 1 1 1c0 1.25.2 2.45.57 3.57a1 1 0 0 1-.25 1z"/></svg></div>
    <div><small>Call Us Today</small><strong>+ 555 014 2288</strong></div>
  </div>
</header>

<section class="hero abs">
  <div class="hero-photo" role="img" aria-label="Businessman holding a tablet with a glowing magnifying glass"></div>
  <h1>Search Engine Optimization</h1>
  <p>Lorem ipsum dolor sit amet, consectetur adipiscing elit, sed do eiusmod tempor incididunt ut labore et dolore magna aliqua.</p>
  <a class="btn" href="#">Get Started</a>
  <svg width="1200" height="689" viewBox="0 0 1200 689" aria-hidden="true">
    <path fill="#ff6509" d="M0,483 C300,600 560,690 760,684 C960,676 1100,620 1200,556 L1200,689 L0,689Z"/>
    <path fill="#fff" d="M0,494 C280,610 520,689 700,689 L0,689Z"/>
  </svg>
  <div class="slider-dots" style="left:565px;top:583px"><i></i><i></i><i></i><i></i></div>
</section>

<div class="about-photo abs">
  <div class="frame"></div>
  <div class="img" role="img" aria-label="Smiling businesswoman in an office with colleagues behind her"></div>
</div>
<div class="about-text abs">
  <h2 class="heading">About Linkvora</h2>
  <div class="rule"></div>
  <p>Sed ut perspiciatis unde omnis iste natus error sit voluptatem accusantium doloremque laudantium, totam rem aperiam, eaque ipsa quae ab illo inventore veritatis et quasi architecto beatae vitae dicta sunt explicabo. Nemo enim ipsam voluptatem quia voluptas sit aspernatur aut odit aut fugit, sed quia consequ untur magni dolores eos qui ratione voluptatem sequi nesciunt. Neque porro quisquam est, qui dolorem ipsum quia dolor sit amet, consectetur, adipisci.</p>
  <a class="btn" href="#">Learn More</a>
</div>

<section class="services abs">
  <h2 class="heading title">We Provide<br>Services</h2>
  <div class="vbar" style="left:395px;top:102px;height:100px"></div>
  <p class="intro">Sed ut perspiciatis unde omnis iste natus error sit voluptatem accusantium dolore mque laudantium, totam rem aperiam, eaque ipsa quae ab illo inventore veritatis et quasi architecto beatae vitae dicta sunt explicabo.</p>

  <div class="card" style="left:112px">
    <svg width="64" height="74" viewBox="0 0 64 74" aria-hidden="true"><circle cx="30" cy="28" r="24" fill="none" stroke="#2f78d6" stroke-width="3"/><circle cx="30" cy="28" r="15" fill="none" stroke="#ff6509" stroke-width="3"/><path d="M30 20l3 6 6 .5-4.5 4 1.5 6-6-3.5-6 3.5 1.5-6-4.5-4 6-.5z" fill="#2f78d6"/><path d="M40 48l10 22-6-3-4 6-7-18M22 50l-6 14" fill="none" stroke="#ff6509" stroke-width="3"/></svg>
    <h3>PREMIUM LINKS</h3>
    <p>Sed ut perspiciatis unde omnis iste natus error sit voluptatem accusa ntium doloremque laudantium, totam rem aperiam, eaque.</p>
    <a class="btn-outline" href="#">Learn More</a>
  </div>
  <div class="card" style="left:447px">
    <svg width="80" height="66" viewBox="0 0 80 66" aria-hidden="true"><rect x="2" y="4" width="76" height="58" fill="none" stroke="#2f78d6" stroke-width="3"/><line x1="2" y1="16" x2="78" y2="16" stroke="#2f78d6" stroke-width="3"/><circle cx="10" cy="10" r="2" fill="#ff6509"/><circle cx="17" cy="10" r="2" fill="#ff6509"/><g fill="none" stroke="#ff6509" stroke-width="2.5"><circle cx="20" cy="29" r="5"/><circle cx="40" cy="29" r="5"/><circle cx="60" cy="29" r="5"/></g><g stroke="#2f78d6" stroke-width="3"><path d="M12 42h16M32 42h16M52 42h16M12 50h16M32 50h16M52 50h16"/></g></svg>
    <h3>MONTHLY LINKS SUBSCRIPTION</h3>
    <p>Sed ut perspiciatis unde omnis iste natus error sit voluptatem accusa ntium doloremque laudantium, totam rem aperiam, eaque.</p>
    <a class="btn-outline" href="#">Learn More</a>
  </div>
  <div class="card" style="left:780px">
    <svg width="74" height="74" viewBox="0 0 74 74" aria-hidden="true"><g fill="none" stroke-width="6" stroke-linecap="round"><path stroke="#2f78d6" d="M34 26l10-10a10 10 0 0 1 14 14L46 42"/><path stroke="#ff6509" d="M40 48L30 58a10 10 0 0 1-14-14l12-12"/><path stroke="#2f78d6" d="M28 46l18-18"/></g></svg>
    <h3>LINK INSERTIONS</h3>
    <p>Sed ut perspiciatis unde omnis iste natus error sit voluptatem accusa ntium doloremque laudantium, totam rem aperiam, eaque.</p>
    <a class="btn-outline" href="#">Learn More</a>
  </div>
</section>

<section class="partners abs" aria-label="Partner agencies">
  <div class="partner" style="left:109px"><span></span></div>
  <div class="partner" style="left:249px"><span></span></div>
  <div class="partner" style="left:390px"><span></span></div>
  <div class="partner" style="left:531px"><span></span></div>
  <div class="partner" style="left:672px"><span></span></div>
  <div class="partner" style="left:813px"><span></span></div>
  <div class="partner" style="left:954px"><span></span></div>
</section>

<section class="testimonials">
  <p class="intro abs">Sed ut perspiciatis unde omnis iste natus error sit voluptatem accusantium dolore mque laudantium, totam rem aperiam, eaque ipsa quae ab illo inventore veritatis et quasi architecto beatae vitae dicta sunt explicabo.</p>
  <div class="vbar" style="left:792px;top:2407px;height:100px"></div>
  <h2 class="heading title abs">Our Client Testimonials</h2>
  <div class="quote" style="left:119px">
    <div class="mark">"</div>
    <p>Sed ut perspiciatis unde omnis iste natus error sit volu ptatem accusantium doloremque laudantium, totam rem aperiam, eaque ipsa quae ab illo inventore veritatis et quasi architecto beatae vitae dicta sunt explicabo. Nemo enim ipsam voluptatem quia voluptas sit asper natur aut odit aut fugit.</p>
    <div class="who">JOHN DEO</div>
  </div>
  <div class="quote" style="left:616px">
    <div class="mark">"</div>
    <p>Sed ut perspiciatis unde omnis iste natus error sit volu ptatem accusantium doloremque laudantium, totam rem aperiam, eaque ipsa quae ab illo inventore veritatis et quasi architecto beatae vitae dicta sunt explicabo. Nemo enim ipsam voluptatem quia voluptas sit asper natur aut odit aut fugit.</p>
    <div class="who">JOHN DEO</div>
  </div>
  <div class="slider-dots" style="left:567px;top:2905px"><i style="background:var(--orange)"></i><i style="background:var(--orange)"></i><i style="background:#fff;border:1px solid var(--orange)"></i><i style="background:var(--orange)"></i><i style="background:var(--orange)"></i></div>
</section>

<section class="blogs abs">
  <h2 class="heading title">Our Latest Blogs</h2>
  <div class="rule"></div>
  <p class="intro">Sed ut perspiciatis unde omnis iste natus error sit voluptatem accusantium doloremque laudantium, totam rem aperiam, eaque ipsa quae ab illo inventore.</p>
  <div class="feature">
    <div class="feature-img" role="img" aria-label="Team meeting around a table with laptops"></div>
    <div class="date">13<small>January</small>2021</div>
    <h3>Sed ut perspiciatis unde omnis iste natus error sit voluptatem</h3>
    <p>Sed ut perspiciatis unde omnis iste natus error sit voluptatemacc usantium doloremque laudantium, totam rem aperiam, eaque ipsa quae ab illo inventore veritatis.</p>
    <a class="btn" href="#">Read More</a>
  </div>
  <article class="post" style="top:234px">
    <div class="thumb" role="img" aria-label="Colleagues discussing work at a desk"></div>
    <h4>Sed ut perspiciatis unde omnis</h4>
    <p>Sed ut perspiciatis unde omnis iste natus error sit voluptatem accusantium dolore mque laudantium.</p>
  </article>
  <article class="post" style="top:423px">
    <div class="thumb" role="img" aria-label="Businessman presenting beside a laptop"></div>
    <h4>Sed ut perspiciatis unde omnis</h4>
    <p>Sed ut perspiciatis unde omnis iste natus error sit voluptatem accusantium dolore mque laudantium.</p>
  </article>
  <article class="post" style="top:611px">
    <div class="thumb" role="img" aria-label="Speaker addressing a small team in an office"></div>
    <h4>Sed ut perspiciatis unde omnis</h4>
    <p>Sed ut perspiciatis unde omnis iste natus error sit voluptatem accusantium dolore mque laudantium.</p>
  </article>
</section>

<footer class="site-footer abs">
  <div class="brand">Linkvora</div>
  <div class="socials" aria-label="Social media"><span></span><span></span><span></span><span></span></div>
  <div class="fcol" style="left:405px">
    <h5>QUICK LINKS</h5>
    <ul><li>Home</li><li>About Us</li><li>Services</li><li>Testimonials</li><li>FAQ</li></ul>
  </div>
  <div class="fcol" style="left:592px">
    <h5>SERVICES</h5>
    <ul><li>Premium Links</li><li>Monthly Links Subscription</li><li>Link Insertions</li></ul>
  </div>
  <div class="fcol contact" style="left:835px">
    <h5>CONTACT US</h5>
    <ul>
      <li><svg width="14" height="20" viewBox="0 0 14 20"><path fill="#fff" d="M7 0a7 7 0 0 0-7 7c0 5 7 13 7 13s7-8 7-13a7 7 0 0 0-7-7zm0 9.5A2.5 2.5 0 1 1 7 4.5a2.5 2.5 0 0 1 0 5z"/></svg><span>123 Lorem ipsum dolor sit<br>amet, consectetur adipiscing</span></li>
      <li><svg width="16" height="16" viewBox="0 0 24 24"><path fill="#fff" d="M6.6 10.8a15.1 15.1 0 0 0 6.6 6.6l2.2-2.2a1 1 0 0 1 1-.25 11.4 11.4 0 0 0 3.6.57 1 1 0 0 1 1 1V20a1 1 0 0 1-1 1A17 17 0 0 1 3 4a1 1 0 0 1 1-1h3.5a1 1 0 0 1 1 1c0 1.25.2 2.45.57 3.57a1 1 0 0 1-.25 1z"/></svg><span>555-019-4470</span></li>
      <li><svg width="16" height="16" viewBox="0 0 24 24"><path fill="#fff" d="M2 5h20v14H2z"/><path d="M2 5l10 8 10-8" fill="none" stroke="#121212" stroke-width="2"/></svg><span>info@linkvoramail.com</span></li>
    </ul>
  </div>
  <hr>
  <div class="copy">© Copyrights Linkvora &nbsp;&nbsp;|&nbsp;&nbsp; All Rights Reserved</div>
</footer>

</body>
</html>
```